Varko label design

Redesign cafe range label for lightly carbonated fruit sodas.
Existing label has not worked in the market place and needs to appeal to 18-40 year olds with an active healthy lifestyle.

Product will remain in current 330ml glass bottle and flavour profile will include current range, sparkling water. It is preferred to maintain a body label only but will consider neck label as well. No over cap concepts will be considered..

Attached final shows brand progress. It has lost its way and needs reinvigorating.

Reason: I have extended the deadline to get proper feed back from others on the designs. Thank you all for your submissions so far. Tom

```html
<!DOCTYPE html>
<html lang="en">
<head>
<meta charset="utf-8">
<title>Varko label range</title>
<link rel="stylesheet" href="https://fonts.googleapis.com/css2?family=Sacramento&family=Oswald:wght@300;500&display=swap">
<style>
  :root {
    --paper: #ffffff;
    --rule: #8a8a8a;
    --raspberry: #e8336b;
    --raspberry-soft: #f28aa6;
    --orange: #f7941d;
    --orange-soft: #fbbf70;
    --lime: #7dc242;
    --lime-soft: #b3dc8a;
    --grapefruit: #ef6b5b;
    --grapefruit-soft: #f5a497;
    --brand-ink: #1a1a1a;
  }
  * { margin: 0; padding: 0; box-sizing: border-box; }
  html, body { width: 1200px; height: 1000px; overflow: hidden; background: var(--paper); }
  .board { position: relative; width: 1200px; height: 1000px; background: var(--paper); }

  .label {
    position: absolute;
    width: 362px; height: 232px;
    border: 1px dashed var(--rule);
    color: var(--tone);
    overflow: hidden;
  }
  .label--raspberry { left: 24px; top: 45px; --tone: var(--raspberry); --soft: var(--raspberry-soft); }
  .label--orange { left: 400px; top: 45px; --tone: var(--orange); --soft: var(--orange-soft); }
  .label--lime { left: 24px; top: 291px; --tone: var(--lime); --soft: var(--lime-soft); }
  .label--grapefruit { left: 400px; top: 291px; --tone: var(--grapefruit); --soft: var(--grapefruit-soft); }

  .brand {
    position: absolute; left: 112px; top: 12px;
    display: flex; align-items: center; gap: 5px;
    font-family: "Oswald", sans-serif; font-weight: 500;
    font-size: 17px; line-height: 1; color: var(--brand-ink); letter-spacing: 0.5px;
    z-index: 2;
  }
  .brand__dot { width: 12px; height: 12px; border-radius: 50%; background: var(--brand-ink); }

  .splash {
    position: absolute; left: 135px; top: 16px;
    width: 172px; height: 128px;
    border-radius: 48% 52% 45% 55% / 55% 45% 55% 45%;
    background: radial-gradient(ellipse at 50% 50%, var(--tone) 0%, var(--soft) 55%, rgba(255,255,255,0) 75%);
    opacity: 0.9;
  }

  .ingredients {
    position: absolute; left: 10px; top: 95px; width: 72px;
    font-family: "Oswald", sans-serif; font-weight: 300;
    font-size: 7px; line-height: 1.15;
  }

  .flavour {
    position: absolute; left: 0; width: 100%;
    font-family: "Sacramento", cursive; font-weight: 400;
    font-size: 50px; line-height: 38px; letter-spacing: 1px;
    white-space: nowrap;
  }
  .label--raspberry .flavour { top: 146px; padding-left: 122px; }
  .label--orange .flavour { top: 154px; padding-left: 124px; }
  .label--lime .flavour { top: 150px; padding-left: 126px; }
  .label--grapefruit .flavour { top: 158px; padding-left: 136px; }

  .volume {
    position: absolute; right: 8px; bottom: 6px;
    font-family: "Oswald", sans-serif; font-weight: 300; font-size: 9px;
  }

  .fruit-mark {
    position: absolute;
    border: 4px solid var(--tone);
    border-radius: 50%;
  }
  .fruit-mark--raspberry { left: 796px; top: 42px; width: 122px; height: 112px; --tone: var(--raspberry); }
  .fruit-mark--orange { left: 810px; top: 255px; width: 92px; height: 92px; --tone: var(--orange); }
  .fruit-mark--lime { left: 792px; top: 448px; width: 136px; height: 100px; --tone: var(--lime); }
  .fruit-mark--grapefruit { left: 788px; top: 630px; width: 146px; height: 146px; --tone: var(--grapefruit); }
</style>
</head>
<body>
<main class="board">

  <section class="label label--raspberry">
    <div class="brand"><span class="brand__dot"></span>Varko</div>
    <div class="splash" role="img" aria-label="Pink watercolour splash with a line-drawn raspberry"></div>
    <p class="ingredients">ingredients: sparkling water, raspberry juice, cranberry juice, cane sugar, natural flavour, citric acid, vitamin c. best served chilled. shake gently before opening.</p>
    <h2 class="flavour">raspberry &amp;<br>cranberry</h2>
    <span class="volume">330 mL</span>
  </section>

  <section class="label label--orange">
    <div class="brand"><span class="brand__dot"></span>Varko</div>
    <div class="splash" role="img" aria-label="Orange watercolour splash with a line-drawn orange"></div>
    <p class="ingredients">ingredients: sparkling water, blood orange juice, orange zest, cane sugar, natural flavour, citric acid, vitamin c. best served chilled. shake gently before opening.</p>
    <h2 class="flavour">blood orange</h2>
    <span class="volume">330 mL</span>
  </section>

  <section class="label label--lime">
    <div class="brand"><span class="brand__dot"></span>Varko</div>
    <div class="splash" role="img" aria-label="Green watercolour splash with a line-drawn lemon"></div>
    <p class="ingredients">ingredients: sparkling water, lemon juice, lemon zest, cane sugar, natural flavour, citric acid, vitamin c. best served chilled. shake gently before opening.</p>
    <h2 class="flavour">lemoncello</h2>
    <span class="volume">330 mL</span>
  </section>

  <section class="label label--grapefruit">
    <div class="brand"><span class="brand__dot"></span>Varko</div>
    <div class="splash" role="img" aria-label="Coral watercolour splash with a line-drawn grapefruit"></div>
    <p class="ingredients">ingredients: sparkling water, pink grapefruit juice, grapefruit zest, cane sugar, natural flavour, citric acid, vitamin c. best served chilled. shake gently before opening.</p>
    <h2 class="flavour">grapefruit</h2>
    <span class="volume">330 mL</span>
  </section>

  <div class="fruit-mark fruit-mark--raspberry" role="img" aria-label="Pink line icon of a raspberry"></div>
  <div class="fruit-mark fruit-mark--orange" role="img" aria-label="Orange line icon of an orange with a leaf"></div>
  <div class="fruit-mark fruit-mark--lime" role="img" aria-label="Green line icon of a lemon"></div>
  <div class="fruit-mark fruit-mark--grapefruit" role="img" aria-label="Coral line icon of a grapefruit with a leaf"></div>

</main>
</body>
</html>
```